Business card for Mortgage broker business

I have already had the logo designed and am needing a great looking business card. My business focus is on servicing clients who may not be able to obtain finance through traditional lenders due to bad credit, short term employment or they just don't fit the banks profile. It needs to be professional, trust worthy but also have a caring fell about it.
I have provided files showing the green and black logo, the white logo(on white background so the file looks blank) and also a file with the white logo with a background of leaves that was made up which will probably be used for a website header.

Industry/Entity Type

Finance

Contact Information for Business Card

Marcus Dalby
Managing Director, Accredited Finance Broker(AFB)
Po Box 817, Pakenham VIC 3810
marcus@kestrelfunding.com.au
www.kestrelfunding.com.au
0438 216 507

Requirements
Nice to have
• I have added a picture of myself as I would like to see some designs with the pic in it, but I'm not sure if I want it on there with the logo's or just the logo's

```html
<!DOCTYPE html>
<html lang="en">
<head>
<meta charset="utf-8">
<title>Kestrel Funding – Business Card</title>
<link href="https://fonts.googleapis.com/css2?family=Open+Sans:wght@400;600;700&display=swap" rel="stylesheet">
<style>
  :root {
    --backdrop: #161616;
    --brand-green: #066837;
    --card-white: #ffffff;
    --text-light: #ffffff;
    --mark-tone: #e9efe9;
  }
  * { margin: 0; padding: 0; box-sizing: border-box; }
  html, body {
    width: 1200px;
    height: 900px;
    overflow: hidden;
    background: var(--backdrop);
    font-family: "Open Sans", Arial, sans-serif;
  }
  .stage { position: relative; width: 1200px; height: 900px; }
  .card {
    position: absolute;
    top: 306px;
    width: 439px;
    height: 271px;
    border-radius: 10px;
  }
  .card-back { left: 149px; background: var(--brand-green); color: var(--text-light); }
  .card-front { left: 609px; background: var(--card-white); }

  .emblem-area {
    position: absolute;
    left: 52px;
    top: 56px;
    width: 166px;
    height: 158px;
    border-radius: 8px;
    background: radial-gradient(circle at 45% 50%, rgba(255,255,255,0.28), rgba(255,255,255,0.06) 70%);
  }
  .contact-block { position: absolute; left: 234px; top: 60px; }
  .holder-name { font-size: 14.5px; font-weight: 700; line-height: 18px; }
  .holder-role { font-size: 11.5px; font-weight: 400; line-height: 15px; }
  .postal { margin-top: 16px; font-size: 11.5px; line-height: 15.5px; }
  .contact-list { list-style: none; margin-top: 11px; font-size: 11.5px; line-height: 16px; }
  .contact-list li { display: flex; align-items: center; gap: 7px; }
  .contact-list svg { width: 9px; height: 9px; fill: var(--text-light); flex: none; }

  .brand-lockup {
    position: absolute;
    left: 0; right: 0; top: 118px;
    display: flex; justify-content: center; align-items: center; gap: 10px;
  }
  .brand-dot { width: 14px; height: 14px; border-radius: 50%; background: var(--brand-green); }
  .brand-name {
    font-size: 30px;
    font-weight: 600;
    color: var(--brand-green);
    letter-spacing: 0.5px;
  }
</style>
</head>
<body>
<main class="stage">
  <section class="card card-back">
    <div class="emblem-area" role="img" aria-label="White line illustration of a dove carrying an olive branch"></div>
    <div class="contact-block">
      <p class="holder-name">Marcus Dalby</p>
      <p class="holder-role">Managing Director</p>
      <p class="postal">Po Box 817<br>Pakenham VIC 3810</p>
      <ul class="contact-list">
        <li><svg viewBox="0 0 10 10" aria-hidden="true"><path d="M2 0.5 L3.8 0.5 L4.4 3 L3.2 3.8 Q4.2 5.9 6.2 6.8 L7 5.6 L9.5 6.2 L9.5 8 Q9.5 9.5 8 9.5 Q0.5 9 0.5 2 Q0.5 0.5 2 0.5 Z"/></svg>0438 216 507</li>
        <li><svg viewBox="0 0 10 10" aria-hidden="true"><path d="M0.5 2 L5 5.5 L9.5 2 L9.5 8.5 L0.5 8.5 Z M0.8 1.3 L9.2 1.3 L5 4.5 Z"/></svg>marcus@kestrelfunding.com.au</li>
        <li><svg viewBox="0 0 10 10" aria-hidden="true"><circle cx="5" cy="5" r="4.5"/></svg>www.kestrelfunding.com.au</li>
      </ul>
    </div>
  </section>

  <section class="card card-front">
    <div class="brand-lockup">
      <span class="brand-dot"></span>
      <span class="brand-name">Kestrel Funding</span>
    </div>
  </section>
</main>
</body>
</html>
```